Business Card Re-Design/Update

We'd like to update out business cards. I've included our current "Style guide" which has the colour scheme of the organisation in it. I've also included the branding files with logos etc in them.

I've also included a copy of one of our existing cards so that you can see how ugly/dated they look. I'd like a fresh modern corporate look.

Target Market(s)

These are for our clients, potential clients, industry contacts - like all business cards

Contact Information for Business Card

Name
Position
Company Address - Level 1, 47 Garnet Lane, Toowong Qld 4066
Direct Phone
mobile
Email
Website -www.korvalnet.com.au
Logo

Colors

Designer to choose colors to be used in the design.

Requirements
Must have
• Main Logo
• Cards will need to be editable to be able to personalize them for each new employee.
Nice to have
• The MapOUT, HandOVER, UpKEEP would be okay to have if they can be sensibly and professionally added to the look without detracting from the main imagery.
• Maybe they could go on the back of the card? will leave this to your creative discretion as to whether/where they fit.
Should not have
• Should not have decorative or script fonts

```html
<!DOCTYPE html>
<html lang="en">
<head>
<meta charset="utf-8">
<title>korvalnet business card</title>
<link rel="stylesheet" href="https://fonts.googleapis.com/css2?family=Ubuntu:wght@400;500;700&display=swap">
<style>
  :root {
    --brand-red: #d81f26;
    --ink-dark: #3a3a3c;
    --ink-text: #333333;
    --paper: #ffffff;
    --map-green: #5ea03a;
    --hand-blue: #2386c8;
    --keep-magenta: #c1208f;
  }
  * { margin: 0; padding: 0; box-sizing: border-box; }
  html, body { width: 1200px; height: 1200px; overflow: hidden; background: var(--paper); }
  body { position: relative; font-family: "Ubuntu", Arial, sans-serif; color: var(--ink-text); }

  .card {
    position: absolute; left: 178px; width: 844px; height: 482px;
    background: var(--paper);
    box-shadow: 0 3px 10px rgba(0,0,0,0.35);
    overflow: hidden;
  }
  .card--front { top: 69px; }
  .card--back { top: 600px; }

  .front-band {
    position: absolute; left: 0; top: 0; width: 100%; height: 363px;
    background: var(--brand-red);
    display: flex; align-items: center; justify-content: center; gap: 22px;
  }
  .wordmark { font-weight: 500; letter-spacing: -1px; line-height: 1; }
  .wordmark-mark { display: inline-block; }
  .front-band .wordmark { font-size: 84px; color: var(--ink-dark); }
  .front-band .wordmark-mark { width: 62px; height: 62px; background: var(--paper); }

  .service-row {
    position: absolute; left: 0; top: 363px; width: 100%; height: 119px;
    display: flex; align-items: center; justify-content: space-around; padding: 0 20px;
  }
  .service { display: flex; align-items: center; gap: 10px; font-size: 38px; font-weight: 500; }
  .service-mark { width: 34px; height: 34px; }
  .service--map { color: var(--map-green); } .service--map .service-mark { background: var(--map-green); }
  .service--hand { color: var(--hand-blue); } .service--hand .service-mark { background: var(--hand-blue); }
  .service--keep { color: var(--keep-magenta); } .service--keep .service-mark { background: var(--keep-magenta); }

  .back-logo {
    position: absolute; left: 0; top: 140px; width: 424px;
    display: flex; flex-direction: column; align-items: center; gap: 22px;
  }
  .back-logo .wordmark-mark { width: 70px; height: 70px; background: var(--brand-red); }
  .back-logo .wordmark { font-size: 66px; color: var(--ink-dark); }

  .divider { position: absolute; left: 423px; top: 84px; width: 2px; height: 352px; background: var(--brand-red); opacity: .85; }

  .person { position: absolute; left: 480px; top: 64px; right: 0; }
  .person-name { font-size: 40px; font-weight: 700; color: var(--brand-red); line-height: 1.1; }
  .person-role { font-size: 19px; color: var(--ink-text); margin-top: 2px; }
  .person-rule { height: 3px; background: var(--brand-red); margin-top: 4px; }

  .address { position: absolute; left: 483px; top: 186px; font-size: 22px; line-height: 32px; color: var(--brand-red); }

  .contact-group { position: absolute; left: 480px; display: flex; align-items: center; gap: 12px; font-size: 20px; line-height: 28px; }
  .contact-icon { width: 26px; height: 26px; flex: none; margin-left: -42px; margin-right: 4px; }
  .contact-group--mobile { top: 276px; }
  .contact-group--office { top: 335px; }
  .contact-group--web { top: 395px; line-height: 24px; }
</style>
</head>
<body>

<section class="card card--front">
  <div class="front-band">
    <span class="wordmark-mark"></span>
    <span class="wordmark">korvalnet</span>
  </div>
  <div class="service-row">
    <div class="service service--map"><span class="service-mark"></span>MapOUT</div>
    <div class="service service--hand"><span class="service-mark"></span>HandOVER</div>
    <div class="service service--keep"><span class="service-mark"></span>UpKEEP</div>
  </div>
</section>

<section class="card card--back">
  <div class="back-logo">
    <span class="wordmark-mark"></span>
    <span class="wordmark">korvalnet</span>
  </div>
  <div class="divider"></div>

  <div class="person">
    <p class="person-name">Mara Tennant</p>
    <p class="person-role">Business Development Manager</p>
    <div class="person-rule"></div>
  </div>

  <p class="address">Level 1, 47 Garnet Lane,<br>Toowong Qld 4066</p>

  <div class="contact-group contact-group--mobile">
    <svg class="contact-icon" viewBox="0 0 24 24" aria-hidden="true"><rect x="7" y="3" width="10" height="18" rx="2" fill="none" stroke="#d81f26" stroke-width="2"/><circle cx="12" cy="17.5" r="1.2" fill="#d81f26"/></svg>
    <p>+61 (0)412 555 018<br>+61 (0)7 3555 0142</p>
  </div>
  <div class="contact-group contact-group--office">
    <svg class="contact-icon" viewBox="0 0 24 24" aria-hidden="true"><path d="M6 3l4 4-2 3c1.5 3 3 4.5 6 6l3-2 4 4-3 3C10 20 4 14 3 6z" fill="#d81f26"/></svg>
    <p>+61 (0)7 3555 0100<br>+61 (0)7 3555 0199</p>
  </div>
  <div class="contact-group contact-group--web">
    <svg class="contact-icon" viewBox="0 0 24 24" aria-hidden="true"><g fill="none" stroke="#d81f26" stroke-width="1.5"><circle cx="12" cy="12" r="9"/><ellipse cx="12" cy="12" rx="4" ry="9"/><path d="M3 12h18M5 7h14M5 17h14"/></g></svg>
    <p>mtennant@korvalnet.com.au<br>www.korvalnet.com.au</p>
  </div>
</section>

</body>
</html>
```